Print Design for Magazine Advertisement

We need a 1/2 page horizontal magazine advertisement for a well respected, local plastic and cosmetic surgery practice. The advertisement will part of a local high-end glossy magazine, Elm Terrace Journal, focusing on key businesses, residents and special interests of local residents living in this the historic district of Hyde Park. district. Advertisement includes mostly text and 1 photo (to be provided) along with images/look and feel which can hopefully be scraped off of the doctor's website. Doctor does not want to add any stock beauty photography or before/after examples. We would like to see ads that are clean, fresh with a slightly traditional feel, a light background color (beige or yellow tone) versus white preferred.
Updates

Just added the content materials and a business card for some background reference to the overall look and feel/style of the Dr's practice. 

Industry/Entity Type

Doctor

Requirements
Must have
• 1) The stylized logo for Larkmoor Cosmetic Surgery Center (from website, www.vostelcosmeticsurgery.example)
2) photo to be provided (preferably placed at right of page)
Nice to have
• Could add a small border design in the corners
Should not have
• no body images, no bright colors

```html
<!DOCTYPE html>
<html lang="en">
<head>
<meta charset="utf-8">
<title>Larkmoor Cosmetic Surgery Center – Half Page Advertisement</title>
<link rel="stylesheet" href="https://fonts.googleapis.com/css2?family=Montserrat:ital,wght@0,400;0,500;0,700;1,700&display=swap">
<style>
  :root {
    --maroon: #7d1532;
    --maroon-deep: #4a0a1c;
    --accent-orange: #e2572b;
    --peach-top: #f2cbb3;
    --peach-bottom: #dc9a72;
    --ink-brown: #7a5849;
    --phone-brown: #7b3d3a;
    --white: #ffffff;
    --stage: #3b3b3b;
  }
  * { margin: 0; padding: 0; box-sizing: border-box; }
  html, body { width: 1200px; height: 1000px; overflow: hidden; }
  body {
    background: var(--stage);
    font-family: "Montserrat", Arial, sans-serif;
    position: relative;
  }
  .ad {
    position: absolute;
    left: 67px; top: 70px;
    width: 1066px; height: 710px;
    background: linear-gradient(to bottom, var(--peach-top) 0%, var(--peach-bottom) 100%);
    overflow: hidden;
    color: var(--maroon);
  }
  .ad__band { position: absolute; left: 0; top: 0; width: 1066px; height: 300px; }
  .headline {
    position: absolute; left: 0; top: 34px; width: 1066px;
    text-align: center; color: var(--white); font-weight: 700;
  }
  .headline__line1 { font-size: 34px; line-height: 46px; }
  .headline__name { font-size: 48px; }
  .headline__line2 { font-size: 34px; line-height: 44px; }
  .headline__tagline { font-size: 20.5px; font-style: italic; font-weight: 700; line-height: 28px; margin-top: 0; }

  .services { position: absolute; left: 56px; top: 227px; width: 580px; }
  .services__title { font-size: 18px; font-weight: 700; letter-spacing: .3px; margin-bottom: 2px; }
  .services__list { list-style: none; font-size: 19.5px; font-weight: 500; line-height: 25.4px; }
  .services__list li { padding-left: 16px; text-indent: -16px; }
  .services__list li::before { content: "• "; }
  .services__list li span { display: block; padding-left: 4px; text-indent: 0; }

  .office-photo {
    position: absolute; left: 711px; top: 174px; width: 257px; height: 188px;
    border-radius: 22px;
    background: linear-gradient(160deg, #c9c2a6 0%, #7f8f5a 45%, #2f4a22 100%);
    box-shadow: 6px 6px 0 var(--maroon-deep);
  }
  .office-caption {
    position: absolute; left: 631px; top: 381px; width: 410px;
    text-align: center; font-size: 14.5px; line-height: 21px; font-weight: 500; color: var(--maroon-deep);
  }
  .honors { position: absolute; left: 586px; top: 494px; width: 490px; text-align: center; color: var(--maroon-deep); }
  .honors__title { font-size: 19px; font-weight: 700; line-height: 26px; color: var(--maroon); }
  .honors__item { font-size: 16px; line-height: 21px; font-weight: 500; }

  .footer { position: absolute; left: 0; top: 605px; width: 1066px; height: 95px; }
  .brand {
    position: absolute; left: 26px; top: 8px; width: 240px;
    text-align: center; color: var(--maroon); font-weight: 700; text-transform: uppercase;
  }
  .brand__line1 { font-size: 27px; line-height: 30px; letter-spacing: 1px; }
  .brand__line2 { font-size: 16px; line-height: 22px; letter-spacing: .8px; }
  .brand__line3 { font-size: 27px; line-height: 30px; letter-spacing: 1px; }
  .footer__divider { position: absolute; top: 10px; width: 1px; height: 74px; background: var(--maroon); }
  .footer__divider--a { left: 280px; }
  .footer__divider--b { left: 705px; }
  .contact { position: absolute; left: 283px; top: 19px; width: 420px; text-align: center; color: var(--ink-brown); font-size: 18.5px; line-height: 30px; }
  .contact strong { font-weight: 500; color: var(--maroon); font-size: 19.5px; }
  .booking { position: absolute; left: 707px; top: 8px; width: 345px; text-align: center; color: var(--maroon); }
  .booking__cta { font-size: 14.5px; font-weight: 500; line-height: 18px; }
  .booking__phone { font-size: 39px; font-weight: 500; line-height: 42px; color: var(--phone-brown); }
  .booking__note { font-size: 11px; font-weight: 500; line-height: 14px; }
</style>
</head>
<body>
  <section class="ad" aria-label="Larkmoor Cosmetic Surgery Center advertisement">
    <svg class="ad__band" viewBox="0 0 1066 300" aria-hidden="true">
      <path fill="var(--accent-orange)" d="M0 0 H1066 V282 C760 280 560 200 300 178 C190 170 90 190 0 215 Z"/>
      <path fill="var(--maroon)" d="M0 0 H1066 V282 C760 270 540 178 270 175 C170 174 90 192 0 215 Z"/>
    </svg>

    <header class="headline">
      <p class="headline__line1"><span class="headline__name">Dr. Martin Vostel</span> is a Board Certified and</p>
      <p class="headline__line2">fellowship - trained Plastic &amp; Reconstructive surgeon</p>
      <p class="headline__tagline">with over 30 years of experience - a trusted choice for Bay Area doctors and their families.</p>
    </header>

    <div class="services">
      <h2 class="services__title">SPECIALIZING IN :</h2>
      <ul class="services__list">
        <li>Breast enhancement, lift and reconstruction</li>
        <li>Body contouring, tummy tucks and liposuction</li>
        <li>Facelift, necklift, browlifts and upper/lower eyelids</li>
        <li>Rhinoplasty (nose) and otoplasty (ear pinning)</li>
        <li>Hair replacement for men and women</li>
        <li>Non-surgical facial treatments – laser treatments,<span>peels, fillers and Velox</span></li>
        <li>Full-time aesthetician, Celia Marwick, with over<span>20 years experience onsite</span></li>
        <li>No long waits in E.R. – private outpatient treatment<span>of minor lacerations and injuries by appointment</span><span>during regular hours</span></li>
      </ul>
    </div>

    <div class="office-photo" role="img" aria-label="Photo of the historic office building framed by oak trees and tropical plants"></div>
    <p class="office-caption">Located steps from Shoreline Blvd., Dr.<br>Vostel's unique and historic Larkmoor<br>office location perfectly sets the tone for a<br>warm and inviting atmosphere.</p>

    <div class="honors">
      <p class="honors__title">COASTAL TOP SURGEONS</p>
      <p class="honors__item">Plastic Surgery (2002 - present)</p>
      <p class="honors__item">Patient Favorite Award winner (2011–present )</p>
    </div>

    <footer class="footer">
      <div class="brand">
        <p class="brand__line1">Larkmoor</p>
        <p class="brand__line2">Cosmetic Surgery</p>
        <p class="brand__line3">Center</p>
      </div>
      <span class="footer__divider footer__divider--a"></span>
      <div class="contact">
        <p>418 S. Alder Ave • Larkmoor, FL 30021</p>
        <p>www.<strong>vostelcosmeticsurgery</strong>.example</p>
      </div>
      <span class="footer__divider footer__divider--b"></span>
      <div class="booking">
        <p class="booking__cta">Call Us To Schedule Your Consultation</p>
        <p class="booking__phone">(555) 014-7600</p>
        <p class="booking__note">Financing through CarePlus Lending is available.</p>
      </div>
    </footer>
  </section>
</body>
</html>
```